Hiring Infographic

We need an infographic for displaying on a website and sharing via social media. Attached is an example of a prior infographic developed for the client for reference (Quiet Meridian). The data for the new infographic is in the attached Mocrosoft Word document about hiring.

Industry/Entity Type

Media

```html
<!DOCTYPE html>
<html lang="en">
<head>
<meta charset="utf-8">
<title>Hiring the Right People – Quiet Meridian</title>
<link rel="stylesheet" href="https://fonts.googleapis.com/css2?family=Oswald:wght@400;500;600&family=PT+Sans:wght@400;700&display=swap">
<style>
:root{
  --navy:#232a4f;
  --orange:#f7a535;
  --sky:#5bb6e6;
  --yellow:#fce23a;
  --banner-grey:#6b6b6b;
  --bg:#f3f3f4;
  --text:#4a4a4a;
  --cyan:#2ec0ef;
  --gold:#fbbd16;
  --pink:#ec9bc4;
  --lime:#b9d23a;
  --red:#e8432c;
  --rule:#dcdcdc;
}
*{margin:0;padding:0;box-sizing:border-box}
html,body{width:759px;height:1200px;overflow:hidden}
body{background:linear-gradient(#fafafa,var(--bg));font-family:"PT Sans",Arial,sans-serif;color:var(--text);position:relative}
.abs{position:absolute}
.header-title{top:25px;left:0;width:759px;text-align:center;font-family:"Oswald",sans-serif;font-weight:500;font-size:17px;color:#fff;letter-spacing:.2px}
.intro{top:96px;left:30px;width:700px;font-size:10.4px;line-height:13px}
.intro p{margin-bottom:12px}
.section-banner{height:36px;background:var(--banner-grey);color:#fff;font-family:"Oswald",sans-serif;font-size:17px;text-align:center;line-height:36px;box-shadow:0 3px 4px rgba(0,0,0,.2)}
.force{width:200px;text-align:center}
.force h2{font-family:"Oswald",sans-serif;font-weight:500;font-size:19px;color:var(--navy);margin-bottom:4px}
.force p{font-size:10.2px;line-height:12.4px}
.rule{left:30px;width:700px;height:2px;background:var(--rule)}
.quality h3{font-family:"Oswald",sans-serif;font-weight:500;font-size:16px;color:var(--navy);line-height:18px}
.quality p{font-size:10.2px;line-height:12px;width:118px}
.evaluate-title{top:1022px;left:18px;font-family:"Oswald",sans-serif;font-weight:500;font-size:33px;line-height:34px;color:#fff}
.evaluate-body{top:1003px;left:222px;width:520px;font-size:10.6px;line-height:12.6px}
.evaluate-body ul{list-style:none;margin-top:12px}
.evaluate-body li.method{font-weight:700;color:var(--navy)}
.evaluate-body li.method::before{content:"• "}
.evaluate-body ol{list-style:none;margin-left:10px}
.evaluate-body ol li{padding-left:14px;position:relative}
.evaluate-body ol li::before{content:"✔";position:absolute;left:0;color:var(--orange);font-size:9px}
</style>
</head>
<body>

<svg class="abs" style="top:0;left:0" width="759" height="80" aria-hidden="true">
  <polygon points="560,0 759,0 759,20 600,14" fill="var(--orange)"/>
  <polygon points="660,0 759,0 759,8" fill="var(--yellow)"/>
  <polygon points="115,12 740,5 700,60 90,70" fill="var(--navy)"/>
  <polygon points="90,70 200,60 215,78 100,80" fill="var(--yellow)"/>
  <polygon points="0,56 90,52 100,80 0,80" fill="var(--orange)" opacity=".0"/>
</svg>
<div class="abs header-title">HIRING THE RIGHT PEOPLE – WHY POTENTIAL TRUMPS EVERYTHING ELSE</div>

<div class="abs intro">
  <p>According to global leadership expert Tomas Herrera-Vidal, potential tops brains, experience and competencies when evaluating employees. It's the number one predictor of success at all levels in every size organization.</p>
  <p>The hallmarks of potential include the ability to adapt and grow. Because companies operate in an increasingly volatile and complex world, they need employees who can easily acclimate to an ever-changing business environment and grow into challenging new roles. Employees must be able to succeed today and tomorrow, regardless of how much things change.</p>
  <p>That's why you can't use a competency-only based evaluation criteria when hiring. It's just impossible to predict the qualifications needed to succeed down the road. Hiring right means identifying candidates with the greatest potential and helping them flourish once they're on your team.</p>
</div>

<div class="abs section-banner" style="top:250px;left:152px;width:456px">THREE FORCES CONTRIBUTING TO SENIOR TALENT SCARCITY</div>

<svg class="abs" style="top:305px;left:60px" width="150" height="120" aria-hidden="true">
  <polygon points="10,20 80,5 135,40 120,110 40,105" fill="var(--sky)"/>
  <polygon points="0,40 60,8 110,20 95,60" fill="var(--orange)"/>
  <polygon points="15,30 110,15 125,90 40,100" fill="var(--navy)"/>
  <g role="img" aria-label="Globe with airplane icon"><circle cx="70" cy="58" r="26" fill="#fff" opacity=".9"/></g>
</svg>
<svg class="abs" style="top:305px;left:310px" width="150" height="120" aria-hidden="true">
  <polygon points="20,15 110,5 140,60 115,110 30,95" fill="var(--sky)"/>
  <polygon points="0,30 70,5 100,30 30,70" fill="var(--orange)"/>
  <polygon points="10,25 120,15 130,95 30,100" fill="var(--navy)"/>
  <g role="img" aria-label="Group of people icon"><rect x="45" y="38" width="50" height="40" rx="8" fill="#fff" opacity=".9"/></g>
</svg>
<svg class="abs" style="top:305px;left:560px" width="150" height="120" aria-hidden="true">
  <polygon points="10,10 90,0 145,45 125,110 25,100" fill="var(--sky)"/>
  <polygon points="60,5 110,0 100,40" fill="var(--orange)"/>
  <polygon points="5,20 120,15 130,95 30,100" fill="var(--navy)"/>
  <circle cx="62" cy="52" r="15" fill="none" stroke="#fff" stroke-width="6"/>
  <line x1="73" y1="63" x2="88" y2="78" stroke="#fff" stroke-width="8" stroke-linecap="round"/>
</svg>

<div class="abs force" style="top:432px;left:30px">
  <h2>GLOBALIZATION</h2>
  <p>With the pace of globalization charging full steam ahead, companies in developed and developing nations must compete for talent like never before. For example, the Global Finance Council predicts 70% of the world's growth by 2016 will come from emerging markets.</p>
</div>
<div class="abs force" style="top:432px;left:280px">
  <h2>DEMOGRAPHICS</h2>
  <p>The percentage of senior executives in the sought-after 35-to-44-year-old age group has been dwindling. During the past decade, this demographic shift primarily affected the U.S. and Europe. However, by 2020, Russia, Canada, South Korea and China will have more workers entering retirement than the workforce.</p>
</div>
<div class="abs force" style="top:432px;left:527px">
  <h2>PIPELINES</h2>
  <p>Companies remain unsure where they will find the next generation of leaders. According to a Harlow Bright Partners 2014 survey of CEOs in 68 countries, 63% of respondents said they were concerned about the future availability of key skills at all levels. In a Northfield Strategy Group study, 56% of executives expect critical gaps in their ability to fill senior managerial roles in coming years.</p>
</div>

<div class="abs rule" style="top:608px"></div>

<div class="abs section-banner" style="top:629px;left:132px;width:496px">IDENTIFYING EMPLOYEE POTENTIAL – THE FIVE CRITICAL QUALITIES</div>

<svg class="abs" style="top:698px;left:33px" width="84" height="84" aria-hidden="true">
  <circle cx="42" cy="42" r="42" fill="var(--cyan)"/>
  <path d="M42 62 C20 46 20 28 32 26 C38 25 42 30 42 33 C42 30 46 25 52 26 C64 28 64 46 42 62Z" fill="#fff"/>
</svg>
<svg class="abs" style="top:698px;left:283px" width="84" height="84" aria-hidden="true">
  <circle cx="42" cy="42" r="42" fill="var(--gold)"/>
  <path d="M16 42 Q42 18 68 42 Q42 66 16 42Z" fill="#fff"/>
  <circle cx="42" cy="42" r="9" fill="var(--gold)"/>
</svg>
<svg class="abs" style="top:698px;left:533px" width="84" height="84" role="img" aria-label="Head with light bulb icon">
  <circle cx="42" cy="42" r="42" fill="var(--pink)"/>
  <circle cx="42" cy="40" r="20" fill="#fff" opacity=".85"/>
</svg>
<svg class="abs" style="top:828px;left:163px" width="84" height="84" role="img" aria-label="Team gathered around a speaker icon">
  <circle cx="42" cy="42" r="42" fill="var(--lime)"/>
  <rect x="22" y="26" width="40" height="34" rx="8" fill="#fff" opacity=".85"/>
</svg>
<svg class="abs" style="top:828px;left:413px" width="84" height="84" aria-hidden="true">
  <circle cx="42" cy="42" r="42" fill="var(--red)"/>
  <path d="M42 18 L64 26 L62 48 C60 60 50 66 42 70 C34 66 24 60 22 48 L20 26Z" fill="none" stroke="#fff" stroke-width="5"/>
  <path d="M42 28 L55 32 L54 48 C52 56 47 59 42 62Z" fill="#fff"/>
</svg>

<div class="abs quality" style="top:688px;left:140px"><h3>MOTIVATION</h3><p>A powerful commitment to pursue unselfish goals. Highly ambitious with a strong desire to excel. Seeks big, collective goals and shows profound personal humility.</p></div>
<div class="abs quality" style="top:688px;left:391px"><h3>CURIOSITY</h3><p>Pursues new experiences, knowledge and candid feedback. Remains open to learning and change.</p></div>
<div class="abs quality" style="top:688px;left:625px"><h3>INSIGHT</h3><p>Gathers and makes sense of information that might lead to new possibilities. Sees connections where others don't.</p></div>
<div class="abs quality" style="top:843px;left:272px"><h3>ENGAGEMENT</h3><p>Uses emotion and logic to communicate a persuasive vision. Connects with work and people.</p></div>
<div class="abs quality" style="top:843px;left:518px"><h3>DETERMINATION</h3><p>Fights for difficult goals despite challenges and bounces back from adversity.</p></div>

<div class="abs rule" style="top:965px"></div>

<svg class="abs" style="top:990px;left:0" width="220" height="200" aria-hidden="true">
  <polygon points="0,120 150,110 120,200 0,200" fill="var(--sky)"/>
  <polygon points="0,150 60,140 40,200 0,200" fill="var(--orange)"/>
  <polygon points="0,10 200,5 150,165 0,170" fill="var(--navy)"/>
  <polygon points="150,165 200,5 210,30 165,180" fill="var(--sky)"/>
</svg>
<div class="abs evaluate-title">HOW TO<br>EVALUATE<br>POTENTIAL</div>

<div class="abs evaluate-body">
  <p>To determine if a candidate believes in self-improvement, enjoys learning and can recovery from missteps, you need to uncover concrete examples by:</p>
  <ul>
    <li class="method">Digging into personal and professional histories</li>
    <li class="method">Conducting in-depth interviews</li>
    <li class="method">Thoroughly checking references</li>
    <li class="method">Asking pointed questions, such as:</li>
  </ul>
  <ol>
    <li>How do you react when someone challenges you?</li>
    <li>How do you invite input from others on your team?</li>
    <li>What do you do to broaden your thinking, experience or personal development?</li>
    <li>How do you foster learning in your organization?</li>
    <li>What steps do you take to seek out the unknown?</li>
  </ol>
</div>

</body>
</html>
```